Etikett Superfruit Sanddorn
Gartenhof Lindmoos suchte ein neues Design in der Kategorie Etiketten und hat ein Projekt auf entwurfsportal.de gestartet.
Zielgruppe
Gartenhof Lindmoos ist ein kleines Unternehmen aus der Steiermark, das sich als Qualitätsführer bei hochwertigen und gesunden Funktionssäften etabliert hat. Unsere Bandbreite geht von international bekannten Wildfrucht Essenzen für die hochwertige Speisenbegleitung bis zu wertvollen Superfruit Säften für die Apotheke.
Nun brauchen wir für den exklusiven Feinkost- und Fachhandel neue Etiketten für unsere Superfruits (Bioqualität aus den besten Lagen). Es handelt sich dabei um eine Top-Positionierung im gehobenen Preissegment.
Mit diesem neuen Design möchten wir die visuelle Abgrenzung unseres Sortiments zwischen Lebensmittel und Feinkost-Vertriebskanal deutlich machen.
Im entwurfsportal Wettbewerb möchten wir mit dem Sanddorn starten.
Aufgabenstellung
Wir wünschen uns ein exklusives und edles Erscheinungsbild des Etiketts (nur Vorderseite), das die hohe Produkt Qualität erkennen lässt. Das Wort „Saft“ soll vermieden werden. Es gibt keine farblichen oder Bild-Vorgaben. Nur zur Info haben wir unser jetziges Etikett hochgeladen, das keinerlei Vorgabe für neue Kreationen darstellt.
Textvorgaben: Sanddorn Pur. careful savouring. Bio.
Die Etikettgröße ist frei wählbar und die Rückseite (noch) nicht wichtig für uns. Danke.

```html
<!DOCTYPE html>
<html lang="de">
<head>
<meta charset="utf-8">
<title>Sanddorn Pur – Etikett</title>
<link href="https://fonts.googleapis.com/css2?family=Antonio:wght@600;700&display=swap" rel="stylesheet">
<style>
  :root {
    --page-bg: #f8f8f8;
    --label-bg: #ffffff;
    --berry-red: #8a3f4f;
    --bio-green: #6b7d12;
    --berry-orange: #f29a1c;
    --berry-deep: #d96f0c;
    --leaf-green: #4f6b3c;
    --text-light: #ffffff;
  }
  * { margin: 0; padding: 0; box-sizing: border-box; }
  html, body {
    width: 1200px;
    height: 1200px;
    overflow: hidden;
    background: var(--page-bg);
  }
  .label {
    position: absolute;
    left: 374px;
    top: 160px;
    width: 457px;
    height: 860px;
    background: var(--label-bg);
    overflow: hidden;
    font-family: "Antonio", sans-serif;
    box-shadow: 0 6px 18px rgba(0,0,0,0.12);
  }
  .product-title {
    position: absolute;
    top: 84px;
    left: 0;
    width: 100%;
    text-align: center;
    color: var(--berry-red);
    font-weight: 700;
    font-size: 88px;
    line-height: 90px;
    letter-spacing: 1px;
  }
  .berry-photo {
    position: absolute;
    left: 0;
    top: 300px;
    width: 100%;
    height: 560px;
    background:
      radial-gradient(ellipse 60% 40% at 35% 55%, var(--berry-orange) 0%, rgba(242,154,28,0.6) 50%, rgba(242,154,28,0) 100%),
      radial-gradient(ellipse 50% 35% at 85% 60%, var(--berry-deep) 0%, rgba(217,111,12,0) 100%),
      linear-gradient(180deg, rgba(255,255,255,1) 0%, rgba(255,255,255,0) 22%, rgba(79,107,60,0.75) 45%, rgba(79,107,60,0.9) 100%);
  }
  .bio-seal {
    position: absolute;
    left: 252px;
    top: 294px;
    width: 120px;
    height: 120px;
    border-radius: 50%;
    background: var(--bio-green);
    display: flex;
    align-items: center;
    justify-content: center;
  }
  .bio-seal::before {
    content: "";
    position: absolute;
    inset: 10px;
    border: 3px solid var(--text-light);
    border-radius: 50%;
  }
  .bio-text {
    color: var(--text-light);
    font-weight: 700;
    font-size: 40px;
    line-height: 1;
    letter-spacing: 1px;
  }
  .brand-name {
    position: absolute;
    left: 247px;
    top: 668px;
    width: 150px;
    text-align center;
    text-align: center;
    color: var(--text-light);
    font-weight: 600;
    font-size: 24px;
    line-height: 28px;
    letter-spacing: 1px;
    text-transform: uppercase;
  }
  .tagline {
    position: absolute;
    left: 0;
    top: 770px;
    width: 100%;
    text-align: center;
    color: var(--text-light);
    font-weight: 600;
    font-size: 34px;
    line-height: 44px;
    letter-spacing: 5px;
    text-transform: uppercase;
  }
</style>
</head>
<body>
  <main class="label">
    <div class="berry-photo" role="img" aria-label="Foto von Zweigen mit orangefarbenen Sanddornbeeren und grünen Blättern"></div>
    <h1 class="product-title">SANDDORN<br>PUR</h1>
    <div class="bio-seal"><span class="bio-text">BIO</span></div>
    <div class="brand-name">Gartenhof<br>Lindmoos</div>
    <p class="tagline">Careful Savouring</p>
  </main>
</body>
</html>
```